Label for Dog Nourishing CBD Balm

Dear Designers,

We are looking for a packaging expert to design our new Hydrating Balm for dogs which contain a relaxing hemp extract (CBD). The product is intended to be massaged on the dog’s paws to make them softer and promote the animal’s well-being :)

Our company is already selling various relaxing cat & dog products, and we would like this new design to reflect the same "style & feeling" as our current products (see attached ZIP file).

Technical aspects:
- The packaging is a 40ml aluminium jar (58mm x 23mm).
- We are looking to design 2 separate labels (one for the front, one for the back)
- The label dimensions should be : 50mm x 50mm
- Please follow technical guidelines from printer (see ZIP file).

Design aspects:
- The design should be compatible with our brand identity (i.e. fluffly, pure, relaxing, positive, clean & natural).
- People should understand what the product "is" and what the product "does" simply from looking at the design.
- The actual balm is white/yellow in color.
- Soft/rounded shapes are preferred.
- Please use our brand's colors (see typo & colors in ZIP file)
- Please use our brand's fonts (see typo & colors in ZIP file)
- Please use our company logo (see ZIP file).
- The design also needs to convey a strong sense of professionalism as we are an animal "healthcare" brand.
- If you want to include a dog picture, we would prefer you to use a picture of our official brand ambassador (see ZIP file).
- Only original work (no plagiarism will be accepted).

Please don't hesitate to send us a message if you have any questions about the brand, the product or the design requirements.

We look forward to seeing your designs & working on this together !

Thanks & regards,
Marcus

Target Market(s)

Dog owners

Font styles to use
Other font styles liked:
• See ZIP file

Requirements
Must have
• Brand fonts (see typo & colors in ZIP file)
Brand colors (see typo & colors in ZIP file)

```html
<!DOCTYPE html>
<html lang="en">
<head>
<meta charset="utf-8">
<title>VerdaBalm Labels – Front and Back</title>
<link href="https://fonts.googleapis.com/css2?family=Nunito:wght@400;600;700;800;900&display=swap" rel="stylesheet">
<style>
  :root {
    --brand-green: #3aa585;
    --brand-green-dark: #2f8f72;
    --ink-dark: #173222;
    --paper: #ffffff;
    --label-silver: #f2f3f3;
  }
  * { margin: 0; padding: 0; box-sizing: border-box; }
  html, body { width: 1200px; height: 1200px; overflow: hidden; background: var(--paper); }
  body { position: relative; font-family: "Nunito", sans-serif; color: var(--brand-green); }

  .side-title {
    position: absolute; top: 278px; transform: translate(-50%, -50%);
    font-weight: 900; font-size: 72px; color: var(--brand-green); letter-spacing: 1px;
  }
  .side-title--front { left: 319px; }
  .side-title--back { left: 894px; }

  .label {
    position: absolute; width: 444px; height: 444px; border-radius: 50%;
    overflow: hidden; background: var(--label-silver);
  }
  .label--front { left: 78px; top: 415px; }
  .label--back { left: 672px; top: 422px; border: 9px solid var(--brand-green); }

  .centered { position: absolute; left: 50%; transform: translate(-50%, -50%); white-space: nowrap; text-align: center; }

  .brand-lockup { display: flex; align-items: center; gap: 10px; }
  .brand-dot { width: 22px; height: 22px; border-radius: 50%; background: var(--brand-green); }
  .brand-name { font-weight: 800; font-size: 46px; color: var(--ink-dark); letter-spacing: 1px; }
  .brand-tagline { font-weight: 700; font-size: 17px; color: var(--brand-green); }

  .front-band { position: absolute; left: 0; right: 0; top: 191px; bottom: 0; background: var(--brand-green); color: var(--paper); }
  .product-name { font-weight: 900; font-size: 46px; }
  .product-type { font-weight: 700; font-size: 28px; }
  .spec { position: absolute; font-weight: 700; font-size: 14px; text-align: center; line-height: 17px; transform: translate(-50%, -50%); }
  .dose { font-weight: 700; font-size: 19px; }
  .benefits { font-weight: 700; font-size: 19px; }

  .back-heading { font-weight: 800; font-size: 14px; color: var(--ink-dark); letter-spacing: -0.2px; }
  .back-copy {
    position: absolute; left: 50%; transform: translateX(-50%); width: 262px;
    font-weight: 400; font-size: 11.5px; line-height: 14.6px; text-align: center; color: var(--brand-green);
  }
  .distributor { position: absolute; left: 100px; top: 326px; font-weight: 800; font-size: 10px; line-height: 13.5px; color: var(--ink-dark); }
  .distributor-title { display: block; padding-left: 14px; margin-bottom: 2px; }
  .back-brand { position: absolute; left: 262px; top: 362px; transform: translateX(-50%); text-align: center; color: var(--ink-dark); }
  .back-brand .brand-name { font-size: 16px; letter-spacing: 0.5px; }
  .back-brand .brand-dot { width: 9px; height: 9px; }
  .back-brand .brand-lockup { gap: 4px; justify-content: center; }
  .back-url { display: block; font-weight: 800; font-size: 8px; margin-top: 6px; }
</style>
</head>
<body>
  <div class="side-title side-title--front">Front</div>
  <div class="side-title side-title--back">Back</div>

  <section class="label label--front" aria-label="Front label">
    <div class="centered brand-lockup" style="top:116px;">
      <span class="brand-dot"></span>
      <span class="brand-name">VERDALIS</span>
    </div>
    <div class="brand-tagline" style="position:absolute; right:108px; top:141px;">For Animals</div>
    <div class="front-band">
      <div class="centered product-name" style="top:31px;">VerdaBalm</div>
      <div class="centered product-type" style="top:65px;">soothing balm</div>
      <div class="spec" style="left:72px; top:105px;">NET WT:<br>40g</div>
      <div class="centered dose" style="top:123px;">CBD 250mg</div>
      <div class="spec" style="left:369px; top:105px;">0%<br>THC</div>
      <div class="centered benefits" style="top:170px;">Repair &nbsp;•&nbsp; Nourish • Protect</div>
    </div>
  </section>

  <section class="label label--back" aria-label="Back label">
    <div class="centered back-heading" style="top:43px;">EVERYDAY RELAXATION</div>
    <p class="back-copy" style="top:54px;">This balm repairs, nourishes and protects your dog's sensitive skin. Its trusted multi-action formula brings relief to fragile areas and soothes temporary irrations (paw pads, elbows, etc.)</p>
    <div class="centered back-heading" style="top:158px;">RECOMMENDED USE:</div>
    <p class="back-copy" style="top:169px;">Rub a small amount of balm in the palm of your hand and apply to sensitive areas as a daily care ritual. Repeat until the product has been completely absorbed.</p>
    <div class="centered back-heading" style="top:258px;">INGREDIENTS:</div>
    <p class="back-copy" style="top:270px;">Shea Butter, Beeswax, Coconut Oil, Hemp Extract (0% THC).</p>
    <div class="distributor">
      <span class="distributor-title">Distributed by:</span>
      VERDA EUROPE KFT.<br>Liget utca 14<br>1071 Budapest<br>Hungary
    </div>
    <div class="back-brand">
      <div class="brand-lockup"><span class="brand-dot"></span><span class="brand-name">VERDALIS</span></div>
      <span class="back-url">www.verdalis.co</span>
    </div>
  </section>
</body>
</html>
```